Nana Bo's needs your help creating a clean, simple, possibly vintage style label for a natural rem...

We need a label for a new product to be sold in local stores. It will be a bottle of fresh Elderberry Syrup which is a natural remedy for the flu, colds, and allergies. Our syrup is different from others in the market as it is fresh, needs to be refrigerated, and does not include preservatives, added sugar, alcohol, or anything artificial. We would like a label with easy to read text, with a clean or vintage look. We would like a 3 inch by 3 inch circle front label with mostly text, not too busy, and possibly a branch of elderberries may be included. We also need a 3 inch by 3 inch circle label for the back of the bottle with the nutrition facts, ingredients, dosage, and specific text. Both labels should be lighter in (background) color to stand out from the dark purple liquid inside. We're leaning towards black for the main text, but open to other ideas that are neutral and not too flashy.The final design should be clear, clean, making the main text visible if in a grocery store refrigerator. It should appeal to all, but mostly to natural minded mothers.
Natural minded mothers

```html
<!DOCTYPE html>
<html lang="en">
<head>
<meta charset="UTF-8">
<title>Nana Bo's Elderberry Syrup – Front Label</title>
<link href="https://fonts.googleapis.com/css2?family=Cormorant+Garamond:wght@500&display=swap" rel="stylesheet">
<style>
  :root {
    --page: #ffffff;
    --ring-teal: #2f5b5a;
    --label-cream: #e2c4a6;
    --rule-cream: #ead6bd;
    --ink: #2a2220;
  }
  html, body {
    margin: 0;
    padding: 0;
    width: 1054px;
    height: 1200px;
    overflow: hidden;
    background: var(--page);
  }
  .canvas {
    position: relative;
    width: 1054px;
    height: 1200px;
  }
  .front-label {
    position: absolute;
    left: 77px;
    top: 150px;
    width: 900px;
    height: 900px;
  }
  .front-label svg { display: block; }
  .label-text {
    font-family: "Cormorant Garamond", Georgia, serif;
    font-weight: 500;
    fill: var(--ink);
  }
  .edge-text {
    font-size: 21px;
    letter-spacing: 1px;
  }
  .maker-name {
    font-size: 38px;
    letter-spacing: 8px;
  }
  .product-name {
    font-size: 86px;
    letter-spacing: 2px;
  }
  .net-weight {
    font-size: 28px;
    letter-spacing: 2px;
  }
</style>
</head>
<body>
<main class="canvas">
  <div class="front-label">
    <svg width="900" height="900" viewBox="0 0 900 900" xmlns="http://www.w3.org/2000/svg">
      <defs>
        <path id="edge-path" d="M 222 678 A 322 322 0 1 1 678 678"/>
      </defs>

      <circle class="ornament-ring" cx="450" cy="450" r="450" fill="var(--ring-teal)" role="img" aria-label="Teal border ring with cream scrollwork ornaments"/>
      <circle class="ring-rule" cx="450" cy="450" r="436" fill="none" stroke="var(--rule-cream)" stroke-width="3"/>

      <circle class="label-face" cx="450" cy="450" r="352" fill="var(--label-cream)"/>
      <circle class="face-rule" cx="450" cy="450" r="352" fill="none" stroke="var(--rule-cream)" stroke-width="4"/>
      <circle class="inner-rule" cx="450" cy="450" r="296" fill="none" stroke="var(--ink)" stroke-width="1.5"/>

      <text class="label-text edge-text">
        <textPath href="#edge-path" startOffset="0" textLength="1500" lengthAdjust="spacing">MADE WITH ORGANIC ELDERBERRIES &amp; SPICES AND LOCAL TEXAS RAW HONEY · IMMUNE BOOSTING · NATURAL REMEDY FOR THE FLU, COLDS, AND ALLERGIES</textPath>
      </text>

      <text class="label-text maker-name" x="454" y="335" text-anchor="middle">NANA BO'S</text>
      <line class="name-rule" x1="360" y1="362" x2="540" y2="362" stroke="var(--ink)" stroke-width="1.5"/>
      <text class="label-text product-name" x="450" y="455" text-anchor="middle">Elderberry</text>
      <text class="label-text product-name" x="450" y="555" text-anchor="middle">Syrup</text>
      <text class="label-text net-weight" x="452" y="670" text-anchor="middle">NET WT 8 FL OZ</text>
    </svg>
  </div>
</main>
</body>
</html>
```